ClipNest Thumbnail for Educational Video About WW2

Please design a bespoke thumbnail for a ClipNest video with the following title:
"Here Lies The Oddest Siege Ever Fought"
The video is about the battle for Castle Morvane, which was a small battle that happened during WW2, in which the Germans fought against themselves for control of Castle Morvane.
The thumbnail should be 1920x1080 pixels

```html
<!DOCTYPE html>
<html lang="en">
<head>
<meta charset="UTF-8">
<title>Here Lies The Oddest Siege Ever Fought</title>
<link rel="stylesheet" href="https://fonts.googleapis.com/css2?family=Anton&display=swap">
<style>
  :root {
    --bg-dark: #231f20;
    --bg-mid: #174a6a;
    --bg-bright: #0a98ea;
    --headline-white: #ffffff;
    --headline-orange: #ff4000;
    --castle-light: #c4bac2;
    --castle-dark: #8c7c80;
    --cutout-edge: #ffffff;
  }
  * { margin: 0; padding: 0; box-sizing: border-box; }
  html, body {
    width: 1200px;
    height: 675px;
    overflow: hidden;
    background: var(--bg-dark);
  }
  .thumbnail {
    position: relative;
    width: 1200px;
    height: 675px;
    overflow: hidden;
    background: linear-gradient(20deg, var(--bg-dark) 15%, var(--bg-mid) 55%, var(--bg-bright) 100%);
  }
  .castle-cutout {
    position: absolute;
    left: 0;
    top: 0;
    width: 1200px;
    height: 675px;
  }
  .headline {
    position: absolute;
    left: 60px;
    top: 118px;
    width: 620px;
    text-align: center;
    font-family: "Anton", "Impact", sans-serif;
    text-transform: uppercase;
    line-height: 1;
  }
  .headline-line { display: block; }
  .headline-white {
    color: var(--headline-white);
    font-size: 98px;
    line-height: 110px;
  }
  .headline-orange {
    color: var(--headline-orange);
    font-size: 136px;
    line-height: 118px;
  }
</style>
</head>
<body>
  <main class="thumbnail">
    <svg class="castle-cutout" viewBox="0 0 1200 675" role="img" aria-label="Photograph of Castle Morvane, a pale stone castle with crenellated towers and arched windows, cut out with a white border">
      <defs>
        <linearGradient id="castleTone" x1="0" y1="0" x2="0.4" y2="1">
          <stop offset="0" stop-color="var(--castle-light)"/>
          <stop offset="1" stop-color="var(--castle-dark)"/>
        </linearGradient>
      </defs>
      <polygon
        points="618,680 622,500 640,485 700,482 742,465 748,172 1062,165 1068,290 1205,262 1205,680"
        fill="url(#castleTone)"
        stroke="var(--cutout-edge)"
        stroke-width="9"
        stroke-linejoin="round"/>
    </svg>

    <h1 class="headline">
      <span class="headline-line headline-white">Here Lies The</span>
      <span class="headline-line headline-orange">Oddest</span>
      <span class="headline-line headline-orange">Siege</span>
      <span class="headline-line headline-white">Ever Fought</span>
    </h1>
  </main>
</body>
</html>
```